Geschäftspapiere für Jobwebseite
Zielgruppe
Hier finden sie alle Informationen zu unserem Unternehmen:
https://www.blauer-kranich.com
Aufgabenstellung
Gerne von den Farben angelehnt an die Website ein modernes Briefpapier gestalten.

```html
<!DOCTYPE html>
<html lang="de">
<head>
<meta charset="utf-8">
<title>Briefpapier – Blauer-Kranich.de</title>
<link href="https://fonts.googleapis.com/css2?family=Fira+Sans:wght@300;400;600;700&display=swap" rel="stylesheet">
<style>
  :root {
    --green: #2a9048;
    --grey-bg: #ebebeb;
    --ink: #4a4a4a;
    --dark: #555555;
    --paper: #ffffff;
  }
  * { box-sizing: border-box; margin: 0; padding: 0; }
  html, body { width: 1200px; height: 1200px; overflow: hidden; }
  body {
    background: var(--grey-bg);
    font-family: "Fira Sans", Arial, sans-serif;
    color: var(--ink);
    position: relative;
  }
  .board-label {
    position: absolute;
    font-size: 15px;
    font-weight: 400;
    color: #222;
  }
  .sheet {
    position: absolute;
    width: 487px;
    background: var(--paper);
    box-shadow: 3px 4px 6px rgba(0,0,0,0.28);
    overflow: hidden;
  }
  .sheet--folded { left: 107px; top: 95px; height: 244px; }
  .sheet--open { left: 107px; top: 418px; height: 688px; }
  .sheet--back { left: 613px; top: 418px; height: 688px; }

  .head-frame {
    position: absolute; left: 0; top: 0; width: 487px; height: 244px;
    border: 7px solid var(--green); border-bottom: none;
  }
  .sheet--open .head-frame { height: 243px; }

  .brand-mark {
    position: absolute; left: 0; width: 100%; top: 26px;
    text-align: center; font-size: 16px; font-weight: 700;
    color: var(--dark); letter-spacing: 0.2px;
  }
  .sender-line {
    position: absolute; left: 58px; top: 124px;
    font-size: 5.4px; color: var(--ink); white-space: nowrap;
  }
  .sender-line strong { color: var(--green); font-weight: 700; }
  .recipient {
    position: absolute; left: 58px; top: 140px;
    font-size: 7.4px; line-height: 10.6px; font-weight: 300; color: #333;
  }
  .subject {
    position: absolute; left: 59px; top: 219px;
    font-size: 10px; font-weight: 700; color: var(--green); letter-spacing: 0.3px;
  }
  .salutation {
    position: absolute; left: 58px; top: 258px;
    font-size: 7.4px; font-weight: 300; color: #333;
  }
  .letter-body {
    position: absolute; left: 58px; top: 288px; width: 302px;
    font-size: 7.2px; line-height: 9.8px; font-weight: 300; color: #333;
  }
  .letter-body p + p { margin-top: 9.8px; }
  .closing {
    position: absolute; left: 58px; top: 572px;
    font-size: 7.2px; font-weight: 300; color: #333;
  }
  .signature {
    position: absolute; left: 58px; top: 584px; width: 100px; height: 28px;
    background: linear-gradient(90deg, rgba(60,60,160,0.10), rgba(60,60,160,0.02));
  }
  .signer {
    position: absolute; left: 58px; top: 612px;
    font-size: 7.2px; font-weight: 300; color: #333;
  }
  .fold-mark {
    position: absolute; left: 0; width: 7px; height: 1px; background: var(--green);
  }
  .company-footer {
    position: absolute; left: 378px; top: 545px;
    font-size: 5.4px; line-height: 9px; font-weight: 300; color: #444;
  }
  .company-footer strong { font-weight: 700; color: var(--dark); }
  .company-footer .gap { height: 9px; }
  .footer-bar {
    position: absolute; left: 379px; top: 682px; width: 79px; height: 6px;
    background: var(--green);
  }

  .back-panel {
    position: absolute; left: 7px; top: 7px; right: 7px; bottom: 7px;
    background: var(--green);
  }
  .back-claim {
    position: absolute; left: 46px; top: 52px;
    font-size: 22.5px; line-height: 30px; font-weight: 400; color: #fff;
  }
  .back-brand {
    position: absolute; right: 38px; top: 606px;
    font-size: 15px; font-weight: 700; color: #fff;
  }
</style>
</head>
<body>

  <div class="board-label" style="left:107px; top:68px;">Gefalzter Brief</div>
  <div class="board-label" style="left:107px; top:389px;">Geöffneter Brief</div>
  <div class="board-label" style="left:613px; top:389px;">Rückseite</div>

  <!-- Folded letter -->
  <div class="sheet sheet--folded">
    <div class="head-frame"></div>
    <div class="brand-mark">BLAUER-KRANICH.de</div>
    <div class="sender-line"><strong>BLAUER-KRANICH.DE</strong> | Lindenallee 12 | 10115 Musterstadt</div>
    <div class="recipient">
      Firma: Musterfirma<br>
      Herr Maximilian Mustermann<br>
      Musterstraße 11<br>
      12345 Musterstadt
    </div>
    <div class="subject">HIER STEHT DER BETREFF</div>
  </div>

  <!-- Open letter -->
  <div class="sheet sheet--open">
    <div class="head-frame"></div>
    <div class="brand-mark">BLAUER-KRANICH.de</div>
    <div class="sender-line"><strong>BLAUER-KRANICH.DE</strong> | Lindenallee 12 | 10115 Musterstadt</div>
    <div class="recipient">
      Firma: Musterfirma<br>
      Herr Maximilian Mustermann<br>
      Musterstraße 11<br>
      12345 Musterstadt
    </div>
    <div class="subject">HIER STEHT DER BETREFF</div>
    <div class="salutation">Sehr geehrter Herr Mustermann,</div>

    <div class="fold-mark" style="top:345px;"></div>
    <div class="fold-mark" style="top:487px;"></div>

    <div class="letter-body">
      <p>Ferem sit, omniendaecte doluptature mo cuptatio. Ebitati ssumqui coria poreici destrum, vidusap elibus qui ipideli tatecabo. Et remporporio di quo ommolup taessit, ius non esequibus et volupiditio optatur ereicat laut et et quae ium int ma sum cori omnimin recus, ent molupti orrores truptassin eos a cor sa sus dolupta sitist laut que plignat.<br>
      Axim exeribus. Pudit arum ium ipiet in ni od mos ent liciam quunt aborporem verferr uptasim ra de int quunt a inimin et il mi, eaque volo bla volo bea qui ius, sum volo Ibus, acepernatem aut explabo rporupta pa qui consediam atus.</p>
      <p>Aximporporum et dolore conecerferia venimet verae sum nobist asintorest, eosant alique volut qui te nullo eum que velitatatis iumque mint ut volupta tquiatemodi dolless itature, et laccuptae pa invelis sequunt, velique abo. Obis sus et officipsamus premquidi blabo. Dollore rnatend untiatu reperion consequam faccaborit faciates sitatenet harunt invenim di sumque.</p>
      <p>Pore oditam identitiis dit estrunt officta tecust pro maionsequis del mos aut quiatur? Icillab ipsapie nihilluptas mo et que sitatiis dolupta quament laborro cuptae. Namus, utendunt.Pictat. Otae nimet faccatur? Erumqui at occum ratquia nos viti con reiunt volorro ommodit, nusam ratiasr itatet pa quistionsed explitem. Nam inis essinve litatib usdandit miliaspedi aces utatem facia volesci alit evel iuntis unt ab ilit autem quam archilluptae</p>
      <p>Sit laut qui tem rerum as reperae prorempedi neces et accullparum fugiae denetur, torernam verepti issinullenis arum re dolessi sum rerum ra di que vel minciam duntio. Aborios molutae praest, corit quiaerci sus andigente sincius si occum fugiae reperibus delicab is sunt magnam is vento to blandiscia quo dolorro vitasped evelest, suntemp oreictor a porepudaeri que conem aut mint alitam si quae volorro rerferia volorepeliti ad ma voluptat acest estrupta si voloriscid millatatae re, offictis aperor maio. Ut liquam erum eum dunt offici dolenih ilibus, id erro et volupta volectent que pla sitis exped maio. Nam sitatur sit qui comnima ximpore consect ibeatatum aut in nulparc hilite nonsequia autemquat.</p>
    </div>

    <div class="closing">Mit freundlichen Grüßen</div>
    <div class="signature" role="img" aria-label="Handschriftliche Unterschrift"></div>
    <div class="signer">Max Mustermann</div>

    <div class="company-footer">
      <strong>BLAUER-KRANICH.de</strong><br>
      Lindenallee 12<br>
      10115 Musterstadt
      <div class="gap"></div>
      <strong>M</strong>&nbsp; info@blauer-kranich.de<br>
      <strong>T</strong>&nbsp; 0123 456 789 0
      <div class="gap"></div>
      Inhaber<br>
      Herr Jonas Falkner
      <div class="gap"></div>
      Amtsgericht Musterstadt<br>
      HRB xxxx<br>
      USt-IdNr. DExxxxxxx
    </div>
    <div class="footer-bar"></div>
  </div>

  <!-- Back side -->
  <div class="sheet sheet--back">
    <div class="back-panel">
      <div class="back-claim">Wir begleiten Dich bei Deinem<br>Jobwechsel als Pflegefachkraft!</div>
      <div class="back-brand">BLAUER-KRANICH.de</div>
    </div>
  </div>

</body>
</html>
```